Business Card Design for a Personal Trainer

I need a business card design for my job as a personal trainer. It should have a unique, modern and exclusive design. On the front there should be only my logo with my name and my job. 0163/2918374 Tobias Kellinger Lindenfeldweg 14 80412 Munich Germany The most important contact information is the web adress. it can be bigger than the rest, but its not necessary. The card should be 8,5cmx5,5cm big. Font: Roboto. Colors: black, white, gray, 56c1ff.

```html
<!DOCTYPE html>
<html lang="de">
<head>
<meta charset="utf-8">
<title>Tobias Kellinger – Business Card</title>
<link href="https://fonts.googleapis.com/css2?family=Roboto:wght@300;400;500&display=swap" rel="stylesheet">
<style>
  :root {
    --page: #ffffff;
    --concrete-light: #b9bfbd;
    --concrete-mid: #a3aaa8;
    --concrete-dark: #8e9694;
    --smoke: #a9bdd6;
    --accent: #56c1ff;
    --brush: #6fdcf5;
    --ink: #111111;
    --white: #f4f6f9;
    --photo-light: #7d7d7d;
    --photo-dark: #2b2b2b;
  }
  * { margin: 0; padding: 0; box-sizing: border-box; }
  html, body { width: 1200px; height: 1200px; overflow: hidden; background: var(--page); }
  body { position: relative; font-family: 'Roboto', sans-serif; }

  .card {
    position: absolute;
    left: 251px;
    width: 698px;
    overflow: hidden;
    background:
      radial-gradient(ellipse at 25% 30%, rgba(255,255,255,0.18), transparent 55%),
      radial-gradient(ellipse at 80% 75%, rgba(0,0,0,0.10), transparent 60%),
      linear-gradient(135deg, var(--concrete-light), var(--concrete-mid) 55%, var(--concrete-dark));
  }
  .card--front { top: 100px; height: 460px; }
  .card--back { top: 600px; height: 451px; }

  /* Front */
  .front__smoke {
    position: absolute; inset: 0;
    background:
      radial-gradient(ellipse 40% 22% at 45% 55%, rgba(169,189,214,0.55), transparent 70%),
      radial-gradient(ellipse 30% 18% at 70% 40%, rgba(169,189,214,0.35), transparent 70%);
  }
  .brand-mark {
    position: absolute; left: 314px; top: 136px;
    width: 70px; height: 70px;
    background: var(--white);
  }
  .brand-name {
    position: absolute; left: 0; right: 0; top: 275px;
    text-align: center;
    font-weight: 400; font-size: 66px; letter-spacing: 0.5px;
    color: var(--white);
    line-height: 1;
    white-space: nowrap;
  }
  .brand-role {
    position: absolute; left: 45px; right: 47px; top: 350px;
    display: flex; align-items: center; gap: 12px;
    font-weight: 400; font-size: 24px; letter-spacing: 5px;
    line-height: 28px;
    color: var(--white);
    white-space: nowrap;
  }
  .brand-role::before, .brand-role::after {
    content: ""; flex: 1; height: 2px; background: var(--white);
  }

  /* Back */
  .back__brush { position: absolute; inset: 0; }
  .back__portrait {
    position: absolute; left: 20px; top: 14px; width: 284px; height: 437px;
    background: linear-gradient(180deg, var(--photo-light) 0%, #505050 40%, var(--photo-dark) 100%);
  }
  .contact { position: absolute; left: 0; top: 0; width: 100%; height: 100%; color: var(--ink); }
  .contact__name {
    position: absolute; left: 337px; top: 85px;
    font-weight: 400; font-size: 35px; line-height: 1; letter-spacing: 0.2px;
    white-space: nowrap;
  }
  .contact__list { list-style: none; }
  .contact__item {
    position: absolute; left: 331px;
    display: flex; align-items: center; gap: 13px;
    font-size: 20px; font-weight: 400; line-height: 24px;
    height: 24px; white-space: nowrap;
  }
  .contact__item--address { top: 154px; }
  .contact__item--phone { top: 204px; }
  .contact__item--mail { top: 248px; }
  .contact__item--web { top: 294px; }
  .contact__icon { width: 22px; height: 22px; flex: none; fill: var(--ink); }
</style>
</head>
<body>

<section class="card card--front" aria-label="Visitenkarte Vorderseite">
  <div class="front__smoke"></div>
  <div class="brand-mark"></div>
  <h1 class="brand-name">TOBIAS KELLINGER</h1>
  <p class="brand-role">PERSONAL TRAINER</p>
</section>

<section class="card card--back" aria-label="Visitenkarte Rückseite">
  <svg class="back__brush" width="698" height="451" viewBox="0 0 698 451" aria-hidden="true">
    <polygon fill="var(--brush)" points="
      150,60 300,48 430,52 560,42 690,50 660,70 698,80 680,108 698,125 670,150
      698,175 675,200 698,230 672,262 698,290 640,300 698,330 600,345 520,360
      420,366 300,372 180,378 90,385 20,380 60,355 0,330 40,300 0,270 50,250
      10,220 60,190 30,160 90,130 60,100 120,80"/>
  </svg>
  <div class="back__portrait" role="img" aria-label="Schwarz-Weiß-Porträtfoto des Trainers mit verschränkten Armen"></div>

  <div class="contact">
    <h2 class="contact__name">TOBIAS KELLINGER</h2>
    <ul class="contact__list">
      <li class="contact__item contact__item--address">
        <svg class="contact__icon" viewBox="0 0 24 24" aria-hidden="true"><path d="M12 1a8 8 0 0 0-8 8c0 6 8 14 8 14s8-8 8-14a8 8 0 0 0-8-8zm0 11a3 3 0 1 1 0-6 3 3 0 0 1 0 6z"/></svg>
        Lindenfeldweg 14, Munich
      </li>
      <li class="contact__item contact__item--phone">
        <svg class="contact__icon" viewBox="0 0 24 24" aria-hidden="true"><path d="M6.6 10.8a15 15 0 0 0 6.6 6.6l2.2-2.2c.3-.3.7-.4 1-.2 1.1.4 2.3.6 3.6.6.6 0 1 .4 1 1V20c0 .6-.4 1-1 1C10.6 21 3 13.4 3 4c0-.6.4-1 1-1h3.5c.6 0 1 .4 1 1 0 1.3.2 2.5.6 3.6.1.3 0 .7-.2 1z"/></svg>
        0163/2918374
      </li>
      <li class="contact__item contact__item--mail">
        <svg class="contact__icon" viewBox="0 0 24 24" aria-hidden="true"><path d="M2 5h20v14H2zm2 2v.5l8 5 8-5V7l-8 5z"/></svg>
        t.kellinger@mailpost.de
      </li>
      <li class="contact__item contact__item--web">
        <svg class="contact__icon" viewBox="0 0 24 24" aria-hidden="true"><path d="M12 2a10 10 0 1 0 0 20 10 10 0 0 0 0-20zm6.9 6h-2.9a15 15 0 0 0-1.4-3.6A8 8 0 0 1 18.9 8zM12 4c.8 1.2 1.5 2.5 1.9 4h-3.8c.4-1.5 1.1-2.8 1.9-4zM4.3 14a8 8 0 0 1 0-4h3.4a16 16 0 0 0 0 4zm.8 2h2.9c.3 1.3.8 2.5 1.4 3.6A8 8 0 0 1 5.1 16zM8 8H5.1a8 8 0 0 1 4.3-3.6C8.8 5.5 8.3 6.7 8 8zm4 12c-.8-1.2-1.5-2.5-1.9-4h3.8c-.4 1.5-1.1 2.8-1.9 4zm2.3-6H9.7a14 14 0 0 1 0-4h4.6a14 14 0 0 1 0 4zm.3 5.6c.6-1.1 1.1-2.3 1.4-3.6h2.9a8 8 0 0 1-4.3 3.6zM16.3 14a16 16 0 0 0 0-4h3.4a8 8 0 0 1 0 4z"/></svg>
        www.tobiaskellinger.de
      </li>
    </ul>
  </div>
</section>

</body>
</html>
```